EverLeafGoods - Stationery, logo provided
Business card, headed paper, comp slip, envelope and A4 folded literature doc wallet
EverLeafGoods - Stationery, logo provided -
Creative Brief
Professional
Mark du Verrand
Les Boulins Rue du Cotil St. Andrews Guernsey GY5 8QT
mark@everleafg.co
www.everleafg.co
The headed paper footer should include the words "Kestrow Limited trading as EverLeafGoods" and possibly on the next line, "Registered in Guernsey - Company No. 71624"
Can be blank or leave to your creativity...

```html
<!DOCTYPE html>
<html lang="en">
<head>
<meta charset="utf-8">
<title>EverLeafGoods Stationery</title>
<link href="https://fonts.googleapis.com/css2?family=Open+Sans:wght@400;600;700&display=swap" rel="stylesheet">
<style>
:root{
  --bg:#000;
  --paper:#fff;
  --green:#3a9a2a;
  --green-light:#8fd14f;
  --green-dark:#1f6e1a;
  --navy:#16245e;
  --ink:#555;
  --grey:#888;
}
*{margin:0;padding:0;box-sizing:border-box}
html,body{width:1200px;height:1104px;overflow:hidden;background:var(--bg);font-family:"Open Sans",Arial,sans-serif}
.canvas{position:relative;width:1200px;height:1104px}
.sheet{position:absolute;background:var(--paper);overflow:hidden}
.sheet svg.deco{position:absolute;left:0;top:0}
.brand{position:absolute;display:flex;align-items:center;gap:6px;font-weight:700;color:var(--green);white-space:nowrap}
.brand .dot{border-radius:50%;background:var(--green);flex:none}
.tagline{position:absolute;font-size:7px;color:var(--grey);white-space:nowrap}
.contact{position:absolute;font-size:6px;line-height:1.5;color:var(--ink);white-space:nowrap}
.contact.top{right:10px;top:10px;text-align:right}
.footer{position:absolute;font-size:7px;line-height:1.6;color:var(--ink);text-align:center}
.caption{position:absolute;font-size:10px;color:#777}

.letterhead-one{left:15px;top:45px;width:323px;height:413px}
.letterhead-two{left:377px;top:45px;width:318px;height:413px}
.envelope{left:742px;top:54px;width:410px;height:170px}
.comp-slip{left:784px;top:168px;width:356px;height:160px;box-shadow:0 0 4px rgba(0,0,0,.4)}
.card{width:120px;height:75px}
.card-a{left:796px;top:473px}
.card-b{left:942px;top:473px}
.card-c{left:870px;top:557px;width:130px;height:50px}
.folder-left{left:24px;top:560px;width:314px;height:518px}
.folder-right{left:338px;top:560px;width:320px;height:518px;border-left:1px solid #ddd}
.notch{position:absolute;left:300px;top:975px}
.slip-title{position:absolute;font-size:7px;letter-spacing:1px;color:var(--grey);font-weight:600}
.card-name{position:absolute;font-size:5px;line-height:1.45;color:#fff;white-space:nowrap}
</style>
</head>
<body>
<main class="canvas">

  <svg width="0" height="0" style="position:absolute">
    <defs>
      <linearGradient id="leafGreen" x1="0" y1="0" x2="0" y2="1">
        <stop offset="0" stop-color="#8fd14f"/>
        <stop offset="1" stop-color="#1f7a1a"/>
      </linearGradient>
      <linearGradient id="leafGreenH" x1="0" y1="0" x2="1" y2="0">
        <stop offset="0" stop-color="#2e8a22"/>
        <stop offset="1" stop-color="#8fd14f"/>
      </linearGradient>
      <linearGradient id="flapGrey" x1="0" y1="0" x2="0" y2="1">
        <stop offset="0" stop-color="#3a3a3a"/>
        <stop offset="1" stop-color="#9a9a9a"/>
      </linearGradient>
    </defs>
  </svg>

  <section class="sheet letterhead-one">
    <svg class="deco" width="323" height="413">
      <path d="M0,0 L34,0 C14,130 14,290 34,413 L0,413 Z" fill="url(#leafGreenH)"/>
      <path d="M34,0 C14,130 14,290 34,413" fill="none" stroke="var(--navy)" stroke-width="4"/>
    </svg>
    <div class="brand" style="left:72px;top:14px;font-size:15px"><span class="dot" style="width:16px;height:16px"></span>EverLeafGoods</div>
    <div class="tagline" style="left:94px;top:36px">Sustainable goods for everyday living</div>
    <div class="contact top">Mark du Verrand<br>Les Boulins, Rue du Cotil<br>St. Andrews, Guernsey<br>GY5 8QT<br>mark@everleafg.co<br>www.everleafg.co</div>
    <div class="footer" style="left:40px;width:283px;top:366px">Kestrow Limited trading as EverLeafGoods<br>Registered in Guernsey - Company No. 71624<br>www.everleafg.co</div>
  </section>
  <div class="caption" style="left:140px;top:474px">Option 1</div>

  <section class="sheet letterhead-two">
    <svg class="deco" width="318" height="413">
      <path d="M0,380 C110,392 210,362 318,322 L318,413 L0,413 Z" fill="url(#leafGreen)"/>
      <path d="M0,380 C110,392 210,362 318,322" fill="none" stroke="var(--navy)" stroke-width="5"/>
    </svg>
    <div class="brand" style="left:70px;top:14px;font-size:15px"><span class="dot" style="width:16px;height:16px"></span>EverLeafGoods</div>
    <div class="tagline" style="left:92px;top:36px">Sustainable goods for everyday living</div>
    <div class="contact top">Mark du Verrand<br>Les Boulins, Rue du Cotil<br>St. Andrews, Guernsey<br>GY5 8QT</div>
    <div class="footer" style="left:150px;width:168px;top:374px;color:#fff;font-size:6px">Kestrow Limited trading as EverLeafGoods<br>Registered in Guernsey - Company No. 71624</div>
  </section>
  <div class="caption" style="left:500px;top:474px">Option 2</div>

  <section class="sheet envelope">
    <svg class="deco" width="410" height="170">
      <path d="M0,0 L410,0 L410,14 L205,62 L0,14 Z" fill="url(#flapGrey)"/>
    </svg>
    <div class="brand" style="left:170px;top:22px;font-size:10px;color:#fff"><span class="dot" style="width:10px;height:10px;background:#fff"></span>EverLeafGoods</div>
  </section>

  <section class="sheet comp-slip">
    <svg class="deco" width="356" height="160">
      <path d="M0,0 L26,0 C10,50 10,110 26,160 L0,160 Z" fill="url(#leafGreenH)"/>
      <path d="M26,0 C10,50 10,110 26,160" fill="none" stroke="var(--navy)" stroke-width="3"/>
      <path d="M26,150 C150,156 260,146 356,138 L356,160 L26,160 Z" fill="url(#leafGreen)"/>
    </svg>
    <div class="brand" style="left:60px;top:8px;font-size:11px"><span class="dot" style="width:11px;height:11px"></span>EverLeafGoods</div>
    <div class="slip-title" style="left:250px;top:12px">WITH COMPLIMENTS</div>
  </section>

  <section class="sheet card card-a">
    <svg class="deco" width="120" height="75">
      <path d="M70,0 C62,25 62,50 70,75 L120,75 L120,0 Z" fill="url(#leafGreen)"/>
    </svg>
    <div class="brand" style="left:5px;top:10px;font-size:5.5px;gap:3px"><span class="dot" style="width:5px;height:5px"></span>EverLeafGoods</div>
    <div class="card-name" style="left:72px;top:22px">Mark du Verrand<br>mark@everleafg.co<br>www.everleafg.co</div>
  </section>
  <section class="sheet card card-b">
    <svg class="deco" width="120" height="75">
      <path d="M0,62 C40,68 80,58 120,52 L120,75 L0,75 Z" fill="url(#leafGreen)"/>
    </svg>
    <div class="brand" style="left:14px;top:14px;font-size:9px"><span class="dot" style="width:9px;height:9px"></span>EverLeafGoods</div>
  </section>
  <section class="sheet card card-c">
    <svg class="deco" width="130" height="50">
      <path d="M66,0 L130,0 L130,50 L66,50 C58,34 58,16 66,0 Z" fill="url(#leafGreen)"/>
    </svg>
    <div class="brand" style="left:4px;top:6px;font-size:5.5px;gap:3px"><span class="dot" style="width:5px;height:5px"></span>EverLeafGoods</div>
    <div class="card-name" style="left:70px;top:10px">Mark du Verrand<br>www.everleafg.co</div>
  </section>

  <section class="sheet folder-left">
    <svg class="deco" width="314" height="518">
      <rect x="0" y="418" width="314" height="100" fill="url(#leafGreen)"/>
    </svg>
    <div class="contact" style="left:0;width:314px;top:372px;text-align:center">Les Boulins, Rue du Cotil, St. Andrews<br>Guernsey GY5 8QT<br>mark@everleafg.co<br>www.everleafg.co</div>
    <div class="brand" style="left:110px;top:474px;font-size:9px;color:#fff"><span class="dot" style="width:9px;height:9px;background:#fff"></span>EverLeafGoods</div>
  </section>

  <section class="sheet folder-right">
    <svg class="deco" width="320" height="518">
      <path d="M0,382 C100,392 210,360 320,342 L320,518 L0,518 Z" fill="url(#leafGreen)"/>
      <path d="M0,382 C100,392 210,360 320,342" fill="none" stroke="var(--navy)" stroke-width="6"/>
    </svg>
    <div class="brand" style="left:100px;top:14px;font-size:15px"><span class="dot" style="width:16px;height:16px"></span>EverLeafGoods</div>
    <div class="tagline" style="left:122px;top:36px">Sustainable goods for everyday living</div>
    <div class="contact" style="left:240px;top:388px;color:#fff">www.everleafg.co</div>
    <div class="brand" style="left:112px;top:474px;font-size:9px;color:#fff"><span class="dot" style="width:9px;height:9px;background:#fff"></span>EverLeafGoods</div>
  </section>
  <svg class="notch" width="76" height="104"><path d="M0,104 L38,0 L76,104 Z" fill="var(--bg)"/></svg>

</main>
</body>
</html>
```